Harrowfield Security Solutions Trade Show

Backdrop for trade show and table cover. Colors to use are red, black and silver/grey . Logo attached. If you are able to view the website and pull any images, that would be great. Website is https://harrowfieldsecuritywx.com/

```html
<!DOCTYPE html>
<html lang="en">
<head>
<meta charset="utf-8">
<title>Harrowfield Security Solutions – Trade Show Backdrop</title>
<link href="https://fonts.googleapis.com/css2?family=Exo+2:wght@700;800;900&display=swap" rel="stylesheet">
<style>
  :root {
    --stage: #e9e9e6;
    --black: #050505;
    --white: #f4f4f4;
    --grey-band: #3f3f41;
    --grey-band-light: #5a5a5c;
    --silver-top: #ffffff;
    --silver-bottom: #b9b9b9;
    --red-top: #e3321e;
    --red-bottom: #a5110c;
    --navy: #1b2030;
  }
  * { margin: 0; padding: 0; box-sizing: border-box; }
  html, body {
    width: 1200px; height: 1200px; overflow: hidden;
    background: var(--stage);
  }
  .backdrop {
    position: absolute; left: 50px; top: 50px;
    width: 1100px; height: 1100px;
    background: var(--black);
    overflow: hidden;
    font-family: "Exo 2", "Arial Black", sans-serif;
  }
  .backdrop-art { position: absolute; inset: 0; }
  .brand {
    position: absolute; left: 0; top: 118px; width: 380px;
    text-align: center; color: var(--navy);
  }
  .brand-name {
    font-weight: 800; font-size: 46px; letter-spacing: 1px; line-height: 1;
  }
  .brand-tagline {
    margin-top: 10px; font-weight: 700; font-size: 16px;
    letter-spacing: 5px; line-height: 1;
  }
  .headline {
    position: absolute; left: 72px; top: 690px;
    font-weight: 900; line-height: 1; text-transform: uppercase;
  }
  .headline span { display: block; }
  .headline-silver {
    font-size: 62px; letter-spacing: 1px;
    background: linear-gradient(var(--silver-top), var(--silver-bottom));
    -webkit-background-clip: text; background-clip: text; color: transparent;
  }
  .headline-red {
    font-size: 70px; margin-top: 6px; letter-spacing: 1px;
    background: linear-gradient(var(--red-top), var(--red-bottom));
    -webkit-background-clip: text; background-clip: text; color: transparent;
  }
  .headline-red + .headline-silver { margin-top: 12px; }
</style>
</head>
<body>
  <main class="backdrop">
    <svg class="backdrop-art" width="1100" height="1100" viewBox="0 0 1100 1100">
      <defs>
        <linearGradient id="photo-tone" gradientUnits="userSpaceOnUse" x1="500" y1="0" x2="1100" y2="1100">
          <stop offset="0" stop-color="#9c9a7e"/>
          <stop offset="0.3" stop-color="#5f6468"/>
          <stop offset="0.6" stop-color="#4a4440"/>
          <stop offset="1" stop-color="#3a3d42"/>
        </linearGradient>
      </defs>

      <!-- brand corner -->
      <g class="brand-corner">
        <path d="M0 0 H270 A130 130 0 0 1 400 130 V330 A200 200 0 0 1 200 530 H0 Z" fill="var(--grey-band)" transform="translate(-30 60)"/>
        <path d="M0 0 H270 A130 130 0 0 1 400 130 V300 A200 200 0 0 1 200 500 H0 Z" fill="var(--white)"/>
      </g>

      <!-- diagonal band shadows -->
      <g class="band-shadows" stroke="var(--grey-band)" stroke-linecap="round" fill="none" transform="translate(-30 40)">
        <line x1="560" y1="-40" x2="1150" y2="340" stroke-width="170"/>
        <line x1="560" y1="300" x2="650" y2="358" stroke-width="150"/>
        <line x1="450" y1="470" x2="1130" y2="910" stroke-width="200"/>
        <line x1="740" y1="560" x2="1150" y2="825" stroke-width="230"/>
        <line x1="720" y1="820" x2="1150" y2="1100" stroke-width="180"/>
      </g>

      <!-- photograph inside diagonal bands -->
      <g role="img" aria-label="Photo of a security guard in a dark uniform seated in a grey vehicle, looking out the open window" stroke="url(#photo-tone)" stroke-linecap="round" fill="none">
        <line x1="560" y1="-40" x2="1150" y2="340" stroke-width="170"/>
        <line x1="560" y1="300" x2="650" y2="358" stroke-width="150"/>
        <line x1="450" y1="470" x2="1130" y2="910" stroke-width="200"/>
        <line x1="740" y1="560" x2="1150" y2="825" stroke-width="230"/>
        <line x1="720" y1="820" x2="1150" y2="1100" stroke-width="180"/>
      </g>
    </svg>

    <div class="brand">
      <div class="brand-name">HARROWFIELD</div>
      <div class="brand-tagline">SECURITY SOLUTIONS</div>
    </div>

    <h1 class="headline">
      <span class="headline-silver">Exceptional</span>
      <span class="headline-red">Security</span>
      <span class="headline-red">Guard</span>
      <span class="headline-silver">Solutions</span>
    </h1>
  </main>
</body>
</html>
```